eBook Cover

Here is the book title: 27 LESSONS A CHURCH LEADER SHOULD
LEARN ABOUT BUDGETS

Here is the subtitle (or author section): A Tithe Harbor eBook

I've attached the tithe harbor logo below.

Target Market(s)

Church Pastors

Requirements
Must have
• Rocket Logo and Tithe Harbor color palette.
Nice to have
• I have attached some sample book covers that I like

```html
<!DOCTYPE html>
<html lang="en">
<head>
<meta charset="utf-8">
<title>27 Lessons A Church Leader Should Learn About Budgets</title>
<link rel="stylesheet" href="https://fonts.googleapis.com/css2?family=Josefin+Sans:wght@400;600;700&family=Oswald:wght@600&display=swap">
<style>
  :root {
    --teal: #6cc0c7;
    --teal-shadow: #4f9aa1;
    --teal-deep: #4a9197;
    --white: #ffffff;
    --yellow: #f3e81b;
    --figure: #3a3a3a;
  }
  * { margin: 0; padding: 0; box-sizing: border-box; }
  html, body { width: 783px; height: 1200px; overflow: hidden; }
  body { background: var(--teal); font-family: "Josefin Sans", sans-serif; }
  .cover { position: relative; width: 783px; height: 1200px; overflow: hidden; background: var(--teal); }
  .cover-shapes { position: absolute; inset: 0; }
  .title { position: absolute; left: 165px; top: 128px; width: 452px; color: var(--white); }
  .title-row { display: flex; justify-content: space-between; align-items: flex-end; gap: 12px; white-space: nowrap; line-height: 0.85; }
  .title-row + .title-row { margin-top: 14px; }
  .num { font-size: 150px; font-weight: 700; letter-spacing: -4px; }
  .w-lessons { font-size: 58px; font-weight: 700; margin-bottom: 28px; }
  .w-church { font-size: 38px; font-weight: 700; margin-bottom: 6px; }
  .w-leader { font-family: "Oswald", sans-serif; font-size: 74px; font-weight: 600; color: var(--yellow); line-height: 0.95; }
  .w-should { font-size: 64px; font-weight: 700; }
  .w-learn { font-size: 42px; font-weight: 600; }
  .w-budgets { font-size: 52px; font-weight: 600; color: var(--yellow); letter-spacing: 1px; }
  .subtitle { position: absolute; right: 166px; top: 494px; font-size: 20px; font-weight: 400; color: var(--white); }
  .brand { position: absolute; left: 400px; top: 1104px; width: 240px; display: flex; align-items: center; justify-content: center; gap: 10px; color: var(--white); font-size: 26px; font-weight: 700; line-height: 1; white-space: nowrap; }
  .brand-dot { width: 12px; height: 12px; border-radius: 50%; background: var(--white); flex: none; }
</style>
</head>
<body>
<main class="cover">
  <svg class="cover-shapes" width="783" height="1200" viewBox="0 0 783 1200">
    <polygon class="title-shadow" fill="var(--teal-shadow)" points="330,140 615,140 783,310 783,900 170,470 170,250" opacity="0.75"/>
    <g role="img" aria-label="Flat illustration of a pastor in a dark cassock and hat with a long patterned shadow">
      <polygon fill="var(--teal-deep)" points="380,560 430,600 783,860 783,1200 560,1200 420,1090"/>
      <rect fill="var(--figure)" x="172" y="520" width="258" height="565" rx="40"/>
    </g>
  </svg>

  <h1 class="title">
    <span class="title-row"><span class="num">27</span><span class="w-lessons">LESSONS</span></span>
    <span class="title-row"><span class="w-church">A CHURCH</span><span class="w-leader">LEADER</span></span>
    <span class="title-row"><span class="w-should">SHOULD</span><span class="w-learn">LEARN</span></span>
    <span class="title-row"><span class="w-budgets">ABOUT BUDGETS</span></span>
  </h1>
  <p class="subtitle">A Tithe Harbor eBook</p>

  <div class="brand">
    <span class="brand-dot"></span>
    <span class="brand-name">Lantern Company</span>
  </div>
</main>
</body>
</html>
```